Mortgage Broker needs a fresh new look for his flyer.

The client is looking for a fresh new look for his mortgage broker business flyer.

* The client is looking for a catch phrase like his competitors... "let your house lend you a hand" or " house rich & cash poor", but I was thinking something like one of the following:

Own Your Home? Get a Loan!
Own a Home? Get a Loan!
Own a Home? Need a loan?
Need a Loan? Use the equity in your home!

* Company website is http://tallvistafunding.com/ for reference.

* within the Logo variation folder, you will find the files named "macOriginalPantone.ai". This is the best full color version of the logo on a transparent background. Please use this as the primary logo.

*The color scheme of the flyer should match that of the primary logo
Updates

Reason: Getting client feedback over Christmas was difficult. The final feedback has now been sent to the final top 3 designers and we are waiting for the designers to come back with the final versions. I only have one day left but it may take longer than that to recieve these designs from all over the world.

Target Market(s)

Target audience are middle age couples or individuals who own their own property as well as the other types of difficult or distressed mortgages.

Industry/Entity Type

Mortgage

Font styles to use
Sans Serif

Requirements
Must have
• Use all the information from the old flyer
Nice to have
• The client sent a 3 fold flyer of a competitor that he likes.
• Please review that but the design doesn't necessarily need to be a 3 fold design.
Should not have
• Darren Lofquist's name should not appear anywhere on the flyer (use the business name instead)

```html
<!DOCTYPE html>
<html lang="en">
<head>
<meta charset="utf-8">
<title>Tall Vista Funding – Folder</title>
<link href="https://fonts.googleapis.com/css2?family=Oswald:wght@400;500;600&family=Open+Sans:wght@400;600&display=swap" rel="stylesheet">
<style>
  :root {
    --backdrop: #a9a9a9;
    --red: #cc1f27;
    --charcoal: #2f2f2f;
    --ink: #1f1f1f;
    --paper: #ffffff;
    --mist: #ececec;
    --rule: #8a8a8a;
  }
  html, body {
    margin: 0; padding: 0;
    width: 1200px; height: 978px;
    overflow: hidden;
    background: var(--backdrop);
  }
  .canvas { position: relative; width: 1200px; height: 978px; }

  .panel { position: absolute; top: 124px; width: 496px; height: 714px; overflow: hidden; }
  .panel--back { left: 108px; }
  .panel--front { left: 604px; }
  .panel__shapes { position: absolute; inset: 0; width: 100%; height: 100%; }

  .brand {
    position: absolute; display: flex; align-items: center; gap: 10px;
    font-family: "Oswald", sans-serif; font-weight: 600;
    color: var(--ink); letter-spacing: 1px; white-space: nowrap;
  }
  .brand__mark { width: 22px; height: 22px; background: var(--red); }
  .panel--back .brand { left: 0; right: 0; justify-content: center; top: 385px; font-size: 36px; }
  .panel--front .brand { left: 0; right: 0; justify-content: center; top: 50px; font-size: 34px; }

  .review { position: absolute; left: 16px; top: 518px; width: 180px; margin: 0;
    font-family: "Oswald", sans-serif; font-weight: 400; font-size: 21px; line-height: 27px;
    color: var(--paper); text-transform: uppercase; border-bottom: 1px solid var(--rule); padding-bottom: 6px; }
  .review__accent { color: var(--red); display: block; }

  .contacts { position: absolute; left: 16px; top: 592px; margin: 0; padding: 0; list-style: none;
    font-family: "Open Sans", sans-serif; color: var(--paper); font-size: 11.5px; line-height: 15px; }
  .contacts li { display: flex; gap: 10px; margin-bottom: 9px; align-items: flex-start; }
  .contacts svg { width: 10px; height: 10px; flex: none; margin-top: 2px; fill: var(--red); }
  .contacts .contacts__phone { font-size: 14px; }

  .socials { position: absolute; left: 330px; top: 680px; display: flex; gap: 8px; }
  .socials span { width: 19px; height: 19px; border-radius: 50%; background: var(--paper); }

  .headline { position: absolute; right: 24px; top: 450px; margin: 0; text-align: right;
    font-family: "Oswald", sans-serif; font-weight: 500; font-size: 54px; line-height: 64px;
    color: var(--paper); text-transform: uppercase; letter-spacing: 0.5px; white-space: nowrap; }
  .intro { position: absolute; right: 24px; top: 606px; margin: 0; text-align: right;
    font-family: "Oswald", sans-serif; font-weight: 400; font-size: 16px; line-height: 26px;
    color: var(--paper); white-space: nowrap; }
  .web { position: absolute; left: 0; right: 0; bottom: 10px; text-align: center;
    font-family: "Open Sans", sans-serif; font-size: 11.5px; color: var(--paper); }
</style>
</head>
<body>
<div class="canvas">

  <section class="panel panel--back">
    <svg class="panel__shapes" viewBox="0 0 496 714" preserveAspectRatio="none" aria-hidden="true">
      <defs>
        <linearGradient id="backPhoto" x1="0" y1="0" x2="0" y2="1">
          <stop offset="0" stop-color="#e9dccf"/>
          <stop offset="0.6" stop-color="#f1e6dc"/>
          <stop offset="1" stop-color="#ececec"/>
        </linearGradient>
      </defs>
      <rect width="496" height="714" fill="var(--mist)"/>
      <rect width="496" height="335" fill="url(#backPhoto)"/>
      <path d="M0,440 C190,466 400,560 492,700 C494,600 495,530 496,458 L496,714 L0,714 Z" fill="var(--red)"/>
      <path d="M0,456 C190,486 376,580 488,714 L0,714 Z" fill="var(--paper)"/>
      <path d="M0,462 C190,494 370,590 478,714 L0,714 Z" fill="var(--charcoal)"/>
    </svg>
    <div role="img" aria-label="Photo: a smiling couple receiving house keys" style="position:absolute;left:0;top:0;width:496px;height:335px"></div>

    <div class="brand"><span class="brand__mark"></span>TALL VISTA FUNDING</div>

    <h2 class="review">Call us for your <span class="review__accent">Mortage Review</span></h2>

    <ul class="contacts">
      <li><svg viewBox="0 0 10 10"><path d="M5 0a3.5 3.5 0 0 0-3.5 3.5C1.5 6 5 10 5 10s3.5-4 3.5-6.5A3.5 3.5 0 0 0 5 0zm0 5a1.5 1.5 0 1 1 0-3 1.5 1.5 0 0 1 0 3z"/></svg><span>1480 Alder Row #212,<br>Vancouver, BC V6K 2P4</span></li>
      <li class="contacts__phone"><svg viewBox="0 0 10 10"><path d="M2 0h2l1 2.5-1.3 1a6 6 0 0 0 2.8 2.8l1-1.3L10 6v2a2 2 0 0 1-2 2C3.6 10 0 6.4 0 2a2 2 0 0 1 2-2z"/></svg><span>+1 604-555-0148</span></li>
      <li><svg viewBox="0 0 10 10"><path d="M0 2h10v6H0z"/></svg><span>info@tallvistafunding.com</span></li>
      <li><svg viewBox="0 0 10 10"><circle cx="5" cy="5" r="5"/></svg><span>www.tallvistafunding.com</span></li>
    </ul>

    <div class="socials" aria-hidden="true"><span></span><span></span><span></span><span></span></div>
  </section>

  <section class="panel panel--front">
    <svg class="panel__shapes" viewBox="0 0 496 714" preserveAspectRatio="none" aria-hidden="true">
      <defs>
        <linearGradient id="frontPhoto" x1="0" y1="0" x2="1" y2="1">
          <stop offset="0" stop-color="#e4dfd8"/>
          <stop offset="0.5" stop-color="#d8c9b6"/>
          <stop offset="1" stop-color="#b9a793"/>
        </linearGradient>
      </defs>
      <rect width="496" height="714" fill="var(--paper)"/>
      <rect y="118" width="496" height="596" fill="url(#frontPhoto)"/>
      <path d="M0,420 C130,320 320,262 496,240 L496,714 L0,714 Z" fill="var(--red)"/>
      <path d="M8,714 C28,510 195,318 496,248 L496,714 Z" fill="var(--paper)"/>
      <path d="M20,714 C40,520 200,330 496,256 L496,714 Z" fill="var(--charcoal)"/>
      <path d="M20,686 L496,676 L496,714 L16,714 Z" fill="var(--red)"/>
    </svg>
    <div role="img" aria-label="Photo: a couple shaking hands with a broker in an office" style="position:absolute;left:0;top:118px;width:496px;height:300px"></div>

    <div class="brand"><span class="brand__mark"></span>TALL VISTA FUNDING</div>

    <h1 class="headline">Own a Home?<br>Need a Loan?</h1>
    <p class="intro">Tall Vista Funding is a Vancouver based equity<br>lender providing real estate loans to property owners.</p>
    <div class="web">www.tallvistafunding.com</div>
  </section>

</div>
</body>
</html>
```